Progressive Architecture and Urban Planning Studio - Stationery Design

The Kestrel Collective: a small boutique Architectural and Urban Planning Studio based in Natal/ RN, Brazil, about to open branches in South Africa and West Africa, established to provide high quality, innovative design and personal client service for projects worldwide. Our approach to Architecture: Minimal - Less is More, so to speak, but with an edge! Strive to produce "clean" projects - stripped of all that can be stripped, no excesses. Got our Logo right here with Pixel Harbor, and hope to do the same with our stationery (were informed that includes business cards, letterhead and envelopes). Since we'll be using two clour schemes, we want at least one using a black background (business card). We'll also allow manipulation of our logo if it helps the final design. Good Luck!

Font styles to use
Other font styles liked:
• Nexa

Colors

Designer to choose colors to be used in the design.

Requirements
Must have
• Business Cards/ Letterheads with the following address:
Rua Olavo Pereira 2741, Vale Dourado, Natal/RN
Should be able to edit it.

```html
<!DOCTYPE html>
<html lang="en">
<head>
<meta charset="utf-8">
<title>The Kestrel Collective — Stationery</title>
<link rel="stylesheet" href="https://fonts.googleapis.com/css2?family=Montserrat:wght@400;600;700&display=swap">
<style>
  :root {
    --backdrop: #e4dac8;
    --paper: #ffffff;
    --card: #000000;
    --ink: #1a1a1a;
    --ink-soft: #3a3a3a;
    --ink-light: #ffffff;
    --brand-red: #d0282c;
    --band-red: #d9575a;
    --band-red-deep: #b8494d;
  }
  * { margin: 0; padding: 0; box-sizing: border-box; }
  html, body {
    width: 1200px; height: 900px; overflow: hidden;
    background: var(--backdrop);
    font-family: "Montserrat", Arial, sans-serif;
  }
  .board { position: relative; width: 1200px; height: 900px; }

  .sheet { position: absolute; background: var(--paper); overflow: hidden; }
  .sheet--dark { background: var(--card); }

  .brand {
    position: absolute; display: flex; align-items: center; gap: 6px;
    font-weight: 600; letter-spacing: 0.04em; text-transform: uppercase;
    color: var(--ink); white-space: nowrap;
  }
  .brand__mark { background: var(--brand-red); flex: none; }
  .sheet--dark .brand { color: var(--ink-light); }

  .address {
    position: absolute; text-transform: uppercase; color: var(--ink-soft);
    line-height: 1.35; letter-spacing: 0.02em;
  }
  .address--right { text-align: right; }
  .sheet--dark .address { color: #d8d8d8; }

  .band {
    position: absolute; left: 0; right: 0; bottom: 0;
    background: linear-gradient(90deg, var(--band-red), var(--band-red-deep));
  }

  /* Letterhead */
  .letterhead { left: 66px; top: 62px; width: 624px; height: 808px; }
  .letterhead .brand { left: 10px; top: 80px; font-size: 16px; }
  .letterhead .brand__mark { width: 12px; height: 12px; }
  .letterhead .address { right: 12px; top: 10px; font-size: 9.5px; }
  .letterhead .band { height: 20px; }

  /* Large envelope */
  .envelope-large { left: 601px; top: 177px; width: 580px; height: 250px; }
  .envelope-large .brand { left: 8px; top: 50px; font-size: 10.5px; }
  .envelope-large .brand__mark { width: 8px; height: 8px; }
  .envelope-large .address { left: 7px; bottom: 21px; font-size: 8.5px; }
  .envelope-large .band { height: 13px; }

  /* DL envelope */
  .envelope-dl { left: 13px; top: 643px; width: 568px; height: 189px; }
  .envelope-dl .brand { left: 10px; top: 40px; font-size: 8px; }
  .envelope-dl .brand__mark { width: 6px; height: 6px; }
  .envelope-dl .address { right: 8px; top: 8px; font-size: 7px; }
  .envelope-dl .band { height: 10px; }

  /* Business cards */
  .card-front { left: 704px; top: 653px; width: 205px; height: 117px; }
  .card-front .brand { left: 4px; top: 32px; font-size: 6.5px; gap: 4px; }
  .card-front .brand__mark { width: 5px; height: 5px; }
  .card-front .holder {
    position: absolute; right: 4px; top: 8px; text-align: right; color: var(--ink-light);
  }
  .holder__name { font-size: 9px; font-weight: 700; letter-spacing: 0.04em; }
  .holder__role { font-size: 6px; color: #cfcfcf; letter-spacing: 0.04em; }
  .card-front .address { right: 4px; bottom: 4px; font-size: 6.5px; }

  .card-back { left: 961px; top: 653px; width: 206px; height: 117px; }
  .card-back .brand {
    left: 0; right: 0; top: 0; bottom: 0; justify-content: center;
    font-size: 11.5px;
  }
  .card-back .brand__mark { width: 9px; height: 9px; }

  /* Standalone mark */
  .brand--display { left: 845px; top: 118px; font-size: 14.5px; }
  .brand--display .brand__mark { width: 11px; height: 11px; }
</style>
</head>
<body>
<main class="board">

  <section class="sheet letterhead" aria-label="Letterhead">
    <div class="brand"><span class="brand__mark"></span>The Kestrel Collective</div>
    <p class="address address--right">Rua Olavo Pereira<br>2741, Vale Dourado, Natal/RN</p>
    <div class="band"></div>
  </section>

  <div class="brand brand--display"><span class="brand__mark"></span>The Kestrel Collective</div>

  <section class="sheet envelope-large" aria-label="Large envelope">
    <div class="brand"><span class="brand__mark"></span>The Kestrel Collective</div>
    <p class="address">Rua Olavo Pereira<br>2741, Vale Dourado, Natal/RN</p>
    <div class="band"></div>
  </section>

  <section class="sheet envelope-dl" aria-label="DL envelope">
    <div class="brand"><span class="brand__mark"></span>The Kestrel Collective</div>
    <p class="address address--right">Rua Olavo Pereira<br>2741, Vale Dourado, Natal/RN</p>
    <div class="band"></div>
  </section>

  <section class="sheet sheet--dark card-front" aria-label="Business card front">
    <div class="brand"><span class="brand__mark"></span>The Kestrel Collective</div>
    <div class="holder">
      <p class="holder__name">NAME</p>
      <p class="holder__role">DESIGNATION</p>
    </div>
    <p class="address address--right">Rua Olavo Pereira<br>2741, Vale Dourado, Natal/RN</p>
  </section>

  <section class="sheet sheet--dark card-back" aria-label="Business card back">
    <div class="brand"><span class="brand__mark"></span>The Kestrel Collective</div>
  </section>

</main>
</body>
</html>
```